Cosmetic injections clinic needs a fresh looking business card

We need a business card using the supplied logo and color scheme to attract future clients to our clinic. It should be modern and fresh, eye catching and not too busy. Simple and to the point is best. I would like two sided designs with the front indicating address and contact information, and the back in full color with white logo and descriptive information also provided.
Target Market(s)
Clients looking for non surgical beauty enhancements.
Contact Information for Business Card
MeloraSkin
14, 618 Birchmont Way
St. Albert, Alberta
K2P 7W3
Phone: 587-412-6630
Email: info@meloraskin.com
Requirements
Must have
- -Logo supplied with the name and address of the clinic
- -Back of card in full color with white logo with A small line of text indicating both of the following: Anti aging consultants and cosmetic injectables
- Located inside the Voyager Wellness Group

```html
<!DOCTYPE html>
<html lang="en">
<head>
<meta charset="utf-8">
<title>MeloraSkin Business Card</title>
<link href="https://fonts.googleapis.com/css2?family=Montserrat:wght@600&family=Barlow:wght@500;600&display=swap" rel="stylesheet">
<style>
  :root {
    --purple: #6a3f9e;
    --pink: #e2429a;
    --white: #ffffff;
    --ground: #ecebef;
    --ink-soft: #f4eefa;
  }
  * { box-sizing: border-box; margin: 0; padding: 0; }
  html, body { width: 1200px; height: 1000px; overflow: hidden; }
  body { background: var(--ground); position: relative; font-family: "Barlow", sans-serif; }

  .card {
    position: absolute;
    width: 600px;
    height: 343px;
    border-radius: 22px;
    overflow: hidden;
    box-shadow: 0 10px 28px rgba(40, 20, 60, 0.18);
  }

  /* Front side */
  .card-front { left: 70px; top: 100px; background: var(--white); }
  .front-shape { position: absolute; inset: 0; width: 100%; height: 100%; }

  .brand { position: absolute; display: flex; align-items: center; gap: 14px; }
  .brand-dot { border-radius: 50%; flex: none; }
  .brand-name {
    font-family: "Montserrat", sans-serif;
    font-weight: 600;
    letter-spacing: 0.5px;
  }
  .card-front .brand { left: 42px; top: 145px; }
  .card-front .brand-dot { width: 58px; height: 58px; background: var(--purple); }
  .card-front .brand-name { font-size: 36px; color: var(--purple); }

  .contact {
    position: absolute;
    left: 385px;
    top: 62px;
    list-style: none;
    color: var(--white);
    font-size: 15px;
    font-weight: 600;
    line-height: 20px;
  }
  .contact li { display: flex; gap: 8px; margin-bottom: 3px; }
  .contact svg { width: 13px; height: 13px; flex: none; margin-top: 3px; fill: var(--white); }
  .contact .icon-spacer { width: 13px; flex: none; }

  /* Back side */
  .card-back { left: 530px; top: 560px; background: var(--pink); }
  .card-back .brand { left: 50%; top: 95px; transform: translateX(-50%); }
  .card-back .brand-dot { width: 72px; height: 72px; background: var(--white); }
  .card-back .brand-name { font-size: 44px; color: var(--white); }

  .info-band {
    position: absolute;
    left: 0; right: 0;
    top: 235px;
    height: 62px;
    background: var(--purple);
    display: flex;
    align-items: center;
    justify-content: center;
    color: var(--white);
    font-weight: 600;
    font-size: 16px;
    line-height: 19px;
    text-align: center;
  }
  .info-band p { width: 250px; }
  .info-divider { width: 1px; height: 34px; background: var(--ink-soft); margin: 0 22px; }
</style>
</head>
<body>

  <section class="card card-front" aria-label="Card front">
    <svg class="front-shape" viewBox="0 0 600 343" preserveAspectRatio="none" aria-hidden="true">
      <path d="M262 0 C300 40 330 120 380 190 C430 260 500 300 560 343 L600 343 L600 0 Z" fill="var(--purple)"/>
      <path d="M238 0 C278 44 306 126 356 196 C404 262 470 302 528 343 L548 343 C490 302 420 258 372 192 C324 124 290 42 256 0 Z" fill="var(--pink)"/>
    </svg>

    <div class="brand">
      <span class="brand-dot"></span>
      <span class="brand-name">MeloraSkin</span>
    </div>

    <ul class="contact">
      <li>
        <svg viewBox="0 0 12 12"><path d="M6 0a4 4 0 0 0-4 4c0 3 4 8 4 8s4-5 4-8a4 4 0 0 0-4-4zm0 5.5A1.5 1.5 0 1 1 6 2.5a1.5 1.5 0 0 1 0 3z"/></svg>
        <span>14, 618 Birchmont Way</span>
      </li>
      <li><span class="icon-spacer"></span><span>St. Albert, Alberta</span></li>
      <li><span class="icon-spacer"></span><span>K2P 7W3</span></li>
      <li>
        <svg viewBox="0 0 12 12"><path d="M2.4 0.6 4.3 2.5 3.3 4a7 7 0 0 0 4.7 4.7l1.5-1 1.9 1.9-1.6 1.9C5 11.2 0.8 7 0.5 2.2z"/></svg>
        <span>587-412-6630</span>
      </li>
      <li>
        <svg viewBox="0 0 12 12"><path d="M0 2h12v8H0zM1 3v.4l5 3.4 5-3.4V3z"/></svg>
        <span>info@meloraskin.com</span>
      </li>
    </ul>
  </section>

  <section class="card card-back" aria-label="Card back">
    <div class="brand">
      <span class="brand-dot"></span>
      <span class="brand-name">MeloraSkin</span>
    </div>

    <div class="info-band">
      <p>Anti aging consultants and cosmetic injectables</p>
      <span class="info-divider"></span>
      <p>Located inside the Voyager Wellness Group</p>
    </div>
  </section>

</body>
</html>
```